Exclusive Furniture Company
Relunda GmbH
Project: Exclusive Furniture Company
Exclusive Furniture Company - General Merchandise
Creative Brief
Professional
Tarin HOLDEVA
CEO
Wolkenriedstrasse 4 8124 Lindwiler - Zürich Switzerland
t.tarin@relunda.ch
www.relunda.ch
Only the symbol R from Logo
Sarah2014 Sarah2014
Dear Designers I need Business Card and Stationary! (not only Business Cards) Thanks in advance Greta
Dear Designer, Please try the black color in other color variants... Thanks in advance! Greta
Dear Designer, Back of the business card is OK Fron part only with logo! see atachemnt: http://relunda.ch/logo/business-card-relunda.png Thanks in advance! Greta PS: I apologize for my English mistakes.

```html
<!DOCTYPE html>
<html lang="en">
<head>
<meta charset="utf-8">
<title>Relunda GmbH – Business Card</title>
<link href="https://fonts.googleapis.com/css2?family=Montserrat:wght@400;500;600;700&display=swap" rel="stylesheet">
<style>
  :root {
    --bg: #b4b4b4;
    --card: #ffffff;
    --ink: #2b2b2b;
    --panel: #333333;
    --red: #c8102e;
    --red-dark: #8e0a1f;
    --muted: #6d6d6d;
    --on-dark: #f2f2f2;
  }
  * { box-sizing: border-box; margin: 0; padding: 0; }
  html, body { width: 1200px; height: 895px; overflow: hidden; }
  body {
    background: var(--bg);
    font-family: "Montserrat", sans-serif;
    display: flex;
    align-items: center;
    justify-content: center;
    gap: 44px;
  }
  .card {
    position: relative;
    width: 540px;
    height: 310px;
    background: var(--card);
    border-radius: 6px;
    overflow: hidden;
    box-shadow: 0 10px 26px rgba(0,0,0,0.18);
  }

  /* Front */
  .card-front .corner-band {
    position: absolute;
    top: 0; right: 0;
    width: 130px; height: 26px;
    background: var(--panel);
  }
  .card-front .corner-band::before {
    content: "";
    position: absolute;
    left: -60px; top: 0;
    width: 60px; height: 26px;
    background: linear-gradient(90deg, rgba(200,16,46,0), var(--red));
  }
  .brand {
    position: absolute;
    left: 50%; top: 50%;
    transform: translate(-50%, -50%);
    display: flex;
    align-items: center;
    gap: 16px;
  }
  .brand-square {
    width: 34px; height: 34px;
    background: var(--red);
  }
  .brand-name {
    font-size: 40px;
    font-weight: 600;
    letter-spacing: 4px;
    color: var(--ink);
  }

  /* Back */
  .back-brand {
    position: absolute;
    left: 26px; top: 26px;
    display: flex;
    align-items: center;
    gap: 10px;
  }
  .back-brand .brand-square { width: 22px; height: 22px; }
  .back-brand .brand-name {
    font-size: 22px;
    letter-spacing: 3px;
    color: var(--red);
  }
  .accent-band {
    position: absolute;
    right: 0; top: 92px;
    width: 170px; height: 14px;
    background: linear-gradient(90deg, rgba(200,16,46,0.15), var(--red) 45%, var(--red-dark));
  }
  .holder {
    position: absolute;
    right: 36px; top: 118px;
    text-align: right;
  }
  .holder-name {
    font-size: 17px;
    font-weight: 500;
    letter-spacing: 1px;
    color: var(--ink);
  }
  .holder-name .first { color: var(--red); }
  .holder-role {
    margin-top: 2px;
    font-size: 9.5px;
    letter-spacing: 1.5px;
    color: var(--muted);
  }
  .contact-panel {
    position: absolute;
    left: 12px; right: 12px; bottom: 12px;
    height: 118px;
    background: var(--panel);
    border-radius: 10px;
    display: grid;
    grid-template-columns: 1fr 1fr 1fr;
  }
  .contact-item {
    display: flex;
    flex-direction: column;
    align-items: center;
    justify-content: center;
    gap: 10px;
    color: var(--on-dark);
    font-size: 10.5px;
    line-height: 1.45;
    text-align: center;
    letter-spacing: 0.4px;
  }
  .contact-item + .contact-item { border-left: 1.5px solid #4a4a4a; }
  .contact-item svg { width: 22px; height: 22px; }
</style>
</head>
<body>

  <section class="card card-front" aria-label="Business card front">
    <div class="corner-band"></div>
    <div class="brand">
      <span class="brand-square"></span>
      <span class="brand-name">RELUNDA</span>
    </div>
  </section>

  <section class="card card-back" aria-label="Business card back">
    <div class="back-brand">
      <span class="brand-square"></span>
      <span class="brand-name">RELUNDA</span>
    </div>
    <div class="accent-band"></div>
    <div class="holder">
      <p class="holder-name"><span class="first">CORIN</span> WALDE</p>
      <p class="holder-role">CREATIVE DIRECTOR</p>
    </div>

    <div class="contact-panel">
      <div class="contact-item">
        <svg viewBox="0 0 24 24" fill="none" stroke="#f2f2f2" stroke-width="1.6" stroke-linejoin="round" aria-hidden="true">
          <path d="M3 9c0-2 2-4 9-4s9 2 9 4l-1 2-4-1V8H8v2l-4 1z"/>
          <path d="M6 12h12l2 8H4z"/>
          <circle cx="12" cy="16" r="2"/>
        </svg>
        <p>014 552 7310<br>014 552 7310</p>
      </div>
      <div class="contact-item">
        <svg viewBox="0 0 24 24" fill="none" stroke="#f2f2f2" stroke-width="1.6" aria-hidden="true">
          <circle cx="12" cy="12" r="9"/>
          <ellipse cx="12" cy="12" rx="4" ry="9"/>
          <path d="M3 12h18M5 7h14M5 17h14"/>
        </svg>
        <p>info@relunda.ch<br>www.relunda.ch</p>
      </div>
      <div class="contact-item">
        <svg viewBox="0 0 24 24" fill="none" stroke="#f2f2f2" stroke-width="1.6" aria-hidden="true">
          <path d="M12 22s-7-7-7-12a7 7 0 0 1 14 0c0 5-7 12-7 12z"/>
          <circle cx="12" cy="10" r="2.5"/>
        </svg>
        <p>27 Lindenhof Court<br>Wolken Road LND</p>
      </div>
    </div>
  </section>

</body>
</html>
```